I teach courses in Lingo Drills in Crisis Care, paramedics, firefighters, nurses and all other Emergency related occupations. I need to let them know that this course is available and post this card on the bulletin boards of fire stations and other related offices. It has to call their attention.

Call

ec2027

• I would like a picture of a paramedic and a nurse. It can also have a firefighter as a second choice. Red is a good color to call attention. I am including a picture of me and a short bio to go on the reverse but this is not a must. I do not want my picture in the front.
I am thinking of an over sized postcard
• The title can be "Lingo Drills in Crisis Care" in full or "Lingo Drills CC's " depending on the fact that the whole name may be too long to make it stand out enough
• I do not know if my picture has come out in the right frame I see the cut is not right in the uploead. You might need to frame it right.

```html
<!DOCTYPE html>
<html lang="en">
<head>
<meta charset="utf-8">
<title>Instructor Bio Card</title>
<link href="https://fonts.googleapis.com/css2?family=Mulish:wght@400;700;800&display=swap" rel="stylesheet">
<style>
  :root {
    --card-bg: #f3f4f6;
    --text-main: #2b2623;
    --link-blue: #1a6fc4;
    --portrait-warm: #b57a4e;
    --portrait-light: #d9a77c;
    --portrait-dark: #5a3a22;
    --glow: rgba(232, 196, 170, 0.35);
  }
  * { box-sizing: border-box; margin: 0; padding: 0; }
  html, body {
    width: 1200px;
    height: 1000px;
    overflow: hidden;
  }
  body {
    background: var(--card-bg);
    font-family: "Mulish", "Century Gothic", sans-serif;
    color: var(--text-main);
  }
  .bio-card {
    position: relative;
    width: 1200px;
    height: 1000px;
    background:
      radial-gradient(ellipse 520px 260px at 50% 72%, var(--glow), transparent 70%),
      var(--card-bg);
  }
  .portrait {
    position: absolute;
    left: 486px;
    top: 150px;
    width: 228px;
    height: 340px;
    background: radial-gradient(ellipse at 50% 45%, var(--portrait-light) 0%, var(--portrait-warm) 45%, var(--portrait-dark) 100%);
  }
  .bio-text {
    position: absolute;
    left: 0;
    top: 540px;
    width: 1200px;
    text-align: center;
    font-size: 23px;
    line-height: 38px;
    letter-spacing: 0.1px;
  }
  .bio-text p + p { margin-top: 38px; }
  .bio-text strong { font-weight: 800; }
  .social-name { color: var(--link-blue); font-weight: 800; }
</style>
</head>
<body>
  <main class="bio-card">
    <div class="portrait" role="img" aria-label="Portrait photo of the instructor"></div>
    <section class="bio-text">
      <p><strong>Marisol Quintero B.A., C.P.C.C.,</strong> brings to the classroom a superb blend of skills,<br>
      knowledge and experience that allows her to design and teach unique courses in Spanish<br>
      as a second language.</p>
      <p>Her native Spanish, "castellano "from Argentina, her many years<br>
      of experience in linguistics and her studies in Life Coaching, Transformational Coaching and<br>
      various other fields assures you a one of a kind language learning experience.</p>
      <p>Find more on <span class="social-name">Linkboard</span> as <strong>Marisol Quintero</strong> or <strong>Call (555) 0142876</strong></p>
    </section>
  </main>
</body>
</html>
```